Counseling Practice Business Card

I need a professional looking business card incorporating my new logo that was just completed. Card needs to incorporate my name and title, description of my specialty, my address, my phone number, my fax number, my email and my website URL. I need to be able to choose design on/with different paper colors and textures.
I do not have a lot of business card ideas so I am open to anything but I want bold,sharp, clear card without additional designs other than my logo (see attached file info). I am open to different color backgrounds or paper colors including black. I do not like traditional brackets around area codes in phone number or dashes between numbers in phone number. Am open to other ways of presenting including periods between numbers as appropriate. I do not know enough to know what I like yet but I want card to coordinate and work together with my logo. My practice emphasizes natural mental health interventions so any use of color (with background paper color or the blue and green in my logo) that elicits nature is nice. In addition to black, any natural brown or wood looking background might be desirable also. Most of the offerings so far look very similar and boring.

Target Market(s)

Potential therapy clients and other professionals

Contact Information for Business Card

Card information:
Marcus T. Whitfield, Ph.D.
Licensed Clinical Psychologist
Integrative Health Coach
4812 Ferndale Pkwy NW
Suite 730
Brackenford, KV 40217
(770) 555-0142 phone
(770) 555-0186 fax
drmarcuswhitfield@kelvora.com
pathbloomcounseling.com

Font styles to use
Serif
Sans Serif
Other font styles liked:
• anything that you think looks crisp, clear and easily readable

Requirements
Must have
• Any color used should coordinate with my logo design (see attached files).
• Card should be printed horizontally so top and bottom are longest sides of rectangle.
• Background color or paper color should complement and highlight logo. Do not like a white background. black, grey, brown or any color my logo would blend well with.
Nice to have
• I would like designer to utilize color to highlight letters/name or phone-fax-web symbols.
• Bottom edge of card could be highlighted if appropriate to an idea.
Should not have
• I would NOT want the card to have a pure white background at all.
• No clear cards.
• Cards should be oriented with long sides on bottom and top, NOT sides. DO NOT LIKE THIS THIN TALL ORIENTATION.

```html
<!DOCTYPE html>
<html lang="en">
<head>
<meta charset="utf-8">
<title>Pathbloom Counseling – Business Card</title>
<link rel="stylesheet" href="https://fonts.googleapis.com/css2?family=Questrial&display=swap">
<style>
  :root {
    --page: #ffffff;
    --card: #ebeced;
    --card-edge: #8a8a8a;
    --ink: #2e2e2e;
    --ink-soft: #3c3c3c;
    --brand-blue: #1d5f9b;
    --icon-fill: #1b5d97;
    --icon-glyph: #ffffff;
  }
  html, body {
    margin: 0;
    padding: 0;
    width: 1200px;
    height: 780px;
    overflow: hidden;
    background: var(--page);
  }
  .card {
    position: absolute;
    left: 34px;
    top: 36px;
    width: 1131px;
    height: 706px;
    box-sizing: border-box;
    background: var(--card);
    border: 1px solid var(--card-edge);
    font-family: "Questrial", sans-serif;
    color: var(--ink);
  }
  .brand {
    position: absolute;
    right: 63px;
    top: 76px;
    text-align: right;
    color: var(--brand-blue);
    font-family: "Questrial", sans-serif;
    line-height: 1;
  }
  .brand__name {
    display: block;
    font-size: 50px;
    letter-spacing: 0.5px;
  }
  .brand__sub {
    display: block;
    margin-top: 4px;
    font-size: 14px;
    letter-spacing: 7.4px;
    text-transform: uppercase;
    margin-right: -7px;
  }
  .identity {
    position: absolute;
    left: 62px;
    top: 196px;
  }
  .identity__name {
    margin: 0;
    font-size: 37px;
    font-weight: 400;
    line-height: 44px;
    color: var(--ink);
    letter-spacing: -0.2px;
  }
  .identity__role {
    margin: 0;
    font-size: 28px;
    line-height: 36px;
    color: var(--ink-soft);
  }
  .contact {
    position: absolute;
    left: 63px;
    top: 369px;
    margin: 0;
    padding: 0;
    list-style: none;
  }
  .contact__item {
    display: flex;
    align-items: center;
    height: 56.5px;
    font-size: 33px;
    color: var(--ink);
    white-space: nowrap;
  }
  .contact__icon {
    flex: none;
    width: 43px;
    height: 43px;
    margin-right: 14px;
  }
  .contact__icon .disc { fill: var(--icon-fill); }
  .contact__icon .glyph { fill: var(--icon-glyph); }
  .contact__icon .stroke { fill: none; stroke: var(--icon-glyph); stroke-width: 1.8; }
</style>
</head>
<body>
  <main class="card">
    <div class="brand">
      <span class="brand__name">Pathbloom</span>
      <span class="brand__sub">Counseling</span>
    </div>

    <section class="identity">
      <h1 class="identity__name">Marcus T. Whitfield, Ph.D.</h1>
      <p class="identity__role">Licensed Clinical Psychologist</p>
      <p class="identity__role">Integrative Health Coach</p>
    </section>

    <ul class="contact">
      <li class="contact__item">
        <svg class="contact__icon" viewBox="0 0 44 44" aria-hidden="true">
          <circle class="disc" cx="22" cy="22" r="22"/>
          <path class="glyph" d="M22 9 L6 23 L9.5 23 L22 12.5 L34.5 23 L38 23 Z"/>
          <path class="glyph" d="M11 24 L22 14.8 L33 24 L33 35 L26 35 L26 27 L18 27 L18 35 L11 35 Z"/>
          <rect class="glyph" x="29" y="11" width="3.5" height="7"/>
        </svg>
        <span>4812 Ferndale Pkwy NW Suite 730 Brackenford, KV 40217</span>
      </li>
      <li class="contact__item">
        <svg class="contact__icon" viewBox="0 0 44 44" aria-hidden="true">
          <circle class="disc" cx="22" cy="22" r="22"/>
          <path class="glyph" d="M17 9 c-3 1 -5 4 -5 9 c0 6 3 13 8 17 c2 1 4 1 6 0 l1.5 -1 l-4 -7 l-2.5 1 c-2 -3 -3 -7 -3 -10 l2.6 -1 l-1.6 -8 z"/>
        </svg>
        <span>770 555 0142</span>
      </li>
      <li class="contact__item">
        <svg class="contact__icon" viewBox="0 0 44 44" aria-hidden="true">
          <circle class="disc" cx="22" cy="22" r="22"/>
          <rect class="glyph" x="14" y="9" width="16" height="7"/>
          <rect class="glyph" x="8" y="17" width="28" height="12" rx="2"/>
          <rect class="glyph" x="14" y="27" width="16" height="9"/>
          <rect class="disc" x="15.5" y="29" width="13" height="1.4"/>
          <rect class="disc" x="15.5" y="32" width="13" height="1.4"/>
        </svg>
        <span>770 555 0186</span>
      </li>
      <li class="contact__item">
        <svg class="contact__icon" viewBox="0 0 44 44" aria-hidden="true">
          <circle class="disc" cx="22" cy="22" r="22"/>
          <rect class="stroke" x="10" y="14" width="24" height="16"/>
          <path class="stroke" d="M10 14 L22 24 L34 14 M10 30 L19 21.5 M34 30 L25 21.5"/>
        </svg>
        <span>drmarcuswhitfield@kelvora.com</span>
      </li>
      <li class="contact__item">
        <svg class="contact__icon" viewBox="0 0 44 44" aria-hidden="true">
          <circle class="disc" cx="22" cy="22" r="22"/>
          <circle class="stroke" cx="22" cy="22" r="14"/>
          <ellipse class="stroke" cx="22" cy="22" rx="6" ry="14"/>
          <path class="stroke" d="M22 8 L22 36 M8 22 L36 22 M10 15 L34 15 M10 29 L34 29"/>
        </svg>
        <span>pathbloomcounseling.com</span>
      </li>
    </ul>
  </main>
</body>
</html>
```